Tri-fold brochue, business card, and stationary design.

Tri-fold brochure: We are looking to get a tri-fold brochure template created so we can add our content on each side of the brochure and then leave these with prospective clients during sales calls.Business card: We would like the business card to have employee name, phone number, and email address on the card. We are open to rounded corners as well.We just redid our website and we'd like all designs to be complementary to our new "Look and feel" of our website.

Contact Information for Business Card

We would like the business card to have employee name, phone number, and email address on the card. We are open to rounded corners as well.

We just redid our website and we'd like all designs to be complementary to our new "Look and feel" of our website.

```html
<!DOCTYPE html>
<html lang="en">
<head>
<meta charset="utf-8">
<title>Harborlink Networks – Business Card</title>
<link href="https://fonts.googleapis.com/css2?family=Roboto:wght@400;700&display=swap" rel="stylesheet">
<style>
  :root {
    --backdrop: #2b2c2f;
    --card: #1b1c1e;
    --brand-blue: #1e96d6;
    --text-light: #f1f2f4;
    --rule: #d9dadc;
  }
  * { margin: 0; padding: 0; box-sizing: border-box; }
  html, body {
    width: 1200px; height: 801px; overflow: hidden;
    background: var(--backdrop);
    font-family: "Roboto", Arial, sans-serif;
  }
  .card {
    position: absolute;
    width: 560px; height: 320px;
    background: var(--card);
    box-shadow: 0 10px 30px rgba(0,0,0,0.45);
  }
  /* Contact side */
  .card-contact { left: 580px; top: 70px; }
  .identity {
    position: absolute; left: 60px; top: 112px;
    color: var(--brand-blue);
  }
  .identity .name { font-size: 34px; font-weight: 700; line-height: 1; }
  .identity .role { font-size: 19px; font-weight: 400; margin-top: 4px; }
  .divider {
    position: absolute; left: 265px; top: 100px;
    width: 2px; height: 76px; background: var(--rule);
  }
  .contact-list {
    position: absolute; left: 290px; top: 110px;
    list-style: none; color: var(--text-light);
    font-size: 18px; line-height: 25px;
  }
  .contact-list li { display: flex; align-items: center; gap: 9px; }
  .icon { width: 15px; height: 15px; fill: var(--brand-blue); flex: none; }
  .address {
    position: absolute; left: 170px; top: 250px;
    display: flex; align-items: center; gap: 8px;
    color: var(--text-light); font-size: 18px;
  }
  /* Brand side */
  .card-brand { left: 70px; top: 420px; }
  .brand-lockup {
    position: absolute; left: 110px; top: 110px;
    display: flex; align-items: center; gap: 18px;
  }
  .brand-dot {
    width: 56px; height: 56px; border-radius: 50%;
    background: var(--brand-blue);
  }
  .brand-name {
    color: var(--brand-blue); font-size: 34px; font-weight: 700;
    line-height: 1.05;
  }
  .web {
    position: absolute; left: 0; right: 0; top: 240px;
    text-align: center; color: var(--text-light);
    font-size: 18px; letter-spacing: 5px;
  }
</style>
</head>
<body>
  <section class="card card-contact">
    <div class="identity">
      <div class="name">Daniel Reyes</div>
      <div class="role">Managing Director</div>
    </div>
    <div class="divider"></div>
    <ul class="contact-list">
      <li>
        <svg class="icon" viewBox="0 0 16 16" aria-hidden="true"><path d="M3.6 1.2l2.3 2.9-1.4 1.6c.9 2 2.6 3.7 4.6 4.6l1.6-1.4 2.9 2.3-1.2 2.3C7 13.6 2.4 9 1.5 2.4z"/></svg>
        555-014-2738
      </li>
      <li>
        <svg class="icon" viewBox="0 0 16 16" aria-hidden="true"><path d="M1 3h14v10H1zM2.5 4.5v.3L8 9l5.5-4.2v-.3z"/></svg>
        dan@harborlinknet.com
      </li>
      <li>
        <svg class="icon" viewBox="0 0 16 16" aria-hidden="true"><circle cx="8" cy="8" r="7"/><path d="M1 8h14M8 1c-3 3-3 11 0 14M8 1c3 3 3 11 0 14" stroke="#1b1c1e" stroke-width="1" fill="none"/></svg>
        harborlinknet.com
      </li>
    </ul>
    <div class="address">
      <svg class="icon" viewBox="0 0 16 16" aria-hidden="true"><path d="M8 0.5a5 5 0 0 0-5 5c0 3.8 5 10 5 10s5-6.2 5-10a5 5 0 0 0-5-5zm0 7a2 2 0 1 1 0-4 2 2 0 0 1 0 4z"/></svg>
      2840 Alder Court&nbsp; Suite B Milford, OH 45150
    </div>
  </section>

  <section class="card card-brand">
    <div class="brand-lockup">
      <div class="brand-dot"></div>
      <div class="brand-name">Harborlink<br>Networks</div>
    </div>
    <div class="web">www.harborlinknet.com</div>
  </section>
</body>
</html>
```